Saffron Lantern Court Business Card

I am looking for a business card desgined for my restaurant. It is an Indian restaurant, we are looking for something thats modern, yet traditional with the indian culture, we are looking for colors that match our logo. The logo is a design of the building with the name of the restaurant. for more information on the restaurant go to www.saffronlanterncourt.example

Industry/Entity Type

Indian Restaurant

Contact Information for Business Card

we are looking for somthing thats modern, yet traditional with the indian culture, we are looking for colors that match our logo. The logo is a design of the building with the name of the restaurant. for more information on the restaurant go to www.saffronlanterncourt.example

Requirements
Must have
• The logo that is attached,
• Name: Harvinder Oberoi,
• address of the restaurant: 7328 West Larkspur Rd, Palo Cresta, Arizona, 85099
• Phone: (602) 555-0147
• Fax: (602) 555-0193
• Restaurant Catering Banquet
• Website: www.SaffronLanternCourt.example
Nice to have
• wanted to get something that goes with the theme of the restaurant, which is traditional but also keep a very professional and modern touch

```html
<!DOCTYPE html>
<html lang="en">
<head>
<meta charset="utf-8">
<title>Saffron Lantern Court – Business Card</title>
<link rel="stylesheet" href="https://fonts.googleapis.com/css2?family=Cinzel:wght@500&family=Oswald:wght@600&family=Open+Sans:wght@400&display=swap">
<style>
  :root {
    --backdrop: #d9d9d9;
    --card-black: #1b1b19;
    --card-black-light: #2a2a26;
    --gold: #e3cf96;
    --gold-deep: #c9ad6c;
    --gold-card: #d8c38c;
    --gold-card-light: #e6d6a8;
    --band-black: #141413;
    --brand-red: #d8452a;
    --ink-dark: #2a2418;
  }
  * { margin: 0; padding: 0; box-sizing: border-box; }
  html, body { width: 1200px; height: 800px; overflow: hidden; }
  body {
    background: var(--backdrop);
    display: flex;
    align-items: center;
    justify-content: center;
    gap: 80px;
  }
  .card {
    position: relative;
    width: 320px;
    height: 560px;
    border-radius: 4px;
    overflow: hidden;
    box-shadow: 0 10px 30px rgba(0,0,0,0.25);
  }
  .card-pattern { position: absolute; inset: 0; }
  /* Front */
  .card-front { background: var(--card-black); }
  .card-front .card-pattern {
    background: radial-gradient(ellipse at 40% 30%, var(--card-black-light), var(--card-black) 75%);
  }
  .front-content {
    position: relative;
    height: 100%;
    padding: 50px 20px 44px;
    display: flex;
    flex-direction: column;
    align-items: center;
  }
  .brand-name {
    font-family: "Cinzel", serif;
    font-weight: 500;
    color: var(--brand-red);
    text-align: center;
    text-transform: uppercase;
    line-height: 1.05;
  }
  .card-front .brand-name { font-size: 30px; letter-spacing: 1px; }
  .person-name {
    margin-top: 28px;
    font-family: "Oswald", sans-serif;
    font-weight: 600;
    font-size: 30px;
    line-height: 1.1;
    letter-spacing: 0.5px;
    color: var(--gold);
    text-transform: uppercase;
    text-align: center;
    white-space: nowrap;
  }
  .contact-list {
    margin-top: 24px;
    list-style: none;
    display: flex;
    flex-direction: column;
    gap: 8px;
    width: 100%;
    align-items: center;
  }
  .contact-row { display: flex; flex-direction: column; align-items: center; gap: 3px; }
  .contact-label {
    background: var(--gold);
    color: var(--ink-dark);
    font-family: "Open Sans", sans-serif;
    font-size: 10px;
    letter-spacing: 1px;
    text-transform: uppercase;
    padding: 1px 22px;
  }
  .contact-value {
    font-family: "Open Sans", sans-serif;
    font-size: 15px;
    color: var(--gold);
    white-space: nowrap;
  }
  .address {
    margin-top: auto;
    font-family: "Open Sans", sans-serif;
    font-style: normal;
    font-size: 20px;
    line-height: 1.3;
    color: var(--gold);
    text-align: center;
    white-space: nowrap;
  }
  /* Back */
  .card-back { background: var(--gold-card); display: flex; flex-direction: column; }
  .card-back .card-pattern {
    bottom: 120px;
    background: radial-gradient(ellipse at 50% 40%, var(--gold-card-light), var(--gold-card) 80%);
  }
  .back-brand {
    position: relative;
    flex: 1;
    display: flex;
    align-items: center;
    justify-content: center;
    padding: 0 30px;
  }
  .card-back .brand-name { font-size: 36px; letter-spacing: 1px; }
  .services-band {
    position: relative;
    height: 120px;
    background: var(--band-black);
    display: flex;
    flex-direction: column;
    align-items: center;
    justify-content: center;
    gap: 6px;
    font-family: "Cinzel", serif;
    font-weight: 500;
    font-size: 17px;
    letter-spacing: 1.5px;
    color: var(--gold-deep);
    text-transform: uppercase;
  }
</style>
</head>
<body>
  <section class="card card-front" aria-label="Business card front">
    <div class="card-pattern" role="img" aria-label="Subtle dark diamond lattice pattern"></div>
    <div class="front-content">
      <div class="brand-name">Saffron<br>Lantern<br>Court</div>
      <h1 class="person-name">Harvinder Oberoi</h1>
      <ul class="contact-list">
        <li class="contact-row"><span class="contact-label">Phone</span><span class="contact-value">(602) 555-0147</span></li>
        <li class="contact-row"><span class="contact-label">Fax</span><span class="contact-value">(602) 555-0193</span></li>
        <li class="contact-row"><span class="contact-label">Web</span><span class="contact-value">www.SaffronLanternCourt.example</span></li>
      </ul>
      <address class="address">7328 West Larkspur Rd,<br>Palo Cresta, Arizona, 85099</address>
    </div>
  </section>

  <section class="card card-back" aria-label="Business card back">
    <div class="card-pattern" role="img" aria-label="Gold diamond lattice pattern"></div>
    <div class="back-brand">
      <div class="brand-name">Saffron<br>Lantern<br>Court</div>
    </div>
    <div class="services-band">
      <span>Restaurant</span>
      <span>Catering Banquet</span>
    </div>
  </section>
</body>
</html>
```